Advertisement flyer for fire sprinkler repair parts. The projected audience are contractors.

I need a flyer advertising specific parts that we are stocking at our company "Meridian Valvecraft Supply." I have attached a picture of our logo. I want the title to say "Fire Pump Repair Parts and Accessories." I want to specifically advertise the following parts: Repack Kits and Repair Parts, Jockey Pumps, Pump Controllers, Casing Relief Valves, Air Release Valves, Suction/Discharge Gauges, Pump Shaft Couplers & Shim Kits, Fire Pump Relief Valves, and QN Listed Pressure Reducing Valves. I have attached pictures of the manufacturers I want to advertise on this flyer. I have also attached pictures of some of the parts we are stocking that I would like to be included somewhere in the flyer. I would like all of the pictures to have a transparent background. Also I would like our phone number :(800)-431-2867, and our website www.tolvenspares.example included. I made my own design that I have Attached. You do not have to go based off this design, but I would like the basic content to be the same. We do have Same- Day shipping as well as Free Tech Support if you can include that anywhere.

```html
<!DOCTYPE html>
<html lang="en">
<head>
<meta charset="utf-8">
<title>Meridian Valvecraft Supply – Fire Pump Repair Parts Flyer</title>
<link rel="stylesheet" href="https://fonts.googleapis.com/css2?family=Montserrat:wght@500&family=Open+Sans:wght@400;600;700&display=swap">
<style>
  :root{
    --page-bg:#e9e9ea;
    --navy:#1f3a93;
    --brand-blue:#1b4fa8;
    --ring-blue:#1e8fdc;
    --accent-red:#e0213a;
    --text-dark:#262a33;
    --white:#ffffff;
    --photo-dark:#3b2a2e;
    --photo-red:#a3232b;
    --photo-grey:#8b8f96;
  }
  *{margin:0;padding:0;box-sizing:border-box}
  html,body{width:1200px;height:800px;overflow:hidden}
  body{background:var(--page-bg);font-family:"Open Sans",Arial,sans-serif;position:relative}

  .flyer{position:absolute;left:300px;top:12px;width:600px;height:776px;background:var(--white);overflow:hidden;box-shadow:0 4px 18px rgba(0,0,0,.18)}

  .hero-photo{position:absolute;left:0;top:0;width:600px;height:400px;
    background:
      radial-gradient(ellipse at 35% 55%, rgba(200,30,40,.85) 0%, rgba(150,25,35,.6) 35%, transparent 65%),
      linear-gradient(160deg,#5a4a50 0%,var(--photo-grey) 30%,var(--photo-red) 60%,var(--photo-dark) 100%);}

  .headline{position:absolute;right:28px;top:38px;text-align:right;color:var(--white);
    font-family:"Montserrat",Arial,sans-serif;font-weight:500;font-size:24px;line-height:1.05;letter-spacing:.3px;
    text-shadow:0 1px 3px rgba(0,0,0,.45)}

  .maker-grid{position:absolute;left:160px;top:240px;width:400px;display:grid;grid-template-columns:repeat(4,88px);gap:10px 12px}
  .maker-tile{height:38px;background:var(--white);border-radius:5px;display:flex;align-items:center;justify-content:center;
    font-size:10px;font-weight:700;color:var(--brand-blue);box-shadow:0 1px 3px rgba(0,0,0,.3)}
  .maker-tile.red{color:var(--accent-red)}

  .panel-shape,.footer-rule{position:absolute;left:0;top:0}

  .footer-photo{position:absolute;right:0;top:672px;width:150px;height:104px;
    background:linear-gradient(200deg,#9aa3ad 0%,#d8c9bd 45%,#eef2f6 100%)}
  .footer-fade{position:absolute;left:0;top:698px;width:600px;height:78px;
    background:linear-gradient(90deg,#ffffff 0%,#f1f5fa 60%,rgba(235,241,248,0) 100%)}

  .brand{position:absolute;left:205px;top:362px;display:flex;align-items:center;gap:12px}
  .brand-square{width:22px;height:22px;background:var(--accent-red)}
  .brand-name{font-size:27px;font-weight:400;color:var(--brand-blue);white-space:nowrap}

  .parts-list{position:absolute;left:38px;top:428px;list-style:none}
  .parts-list li{display:flex;align-items:center;gap:12px;height:23.5px;font-size:13.5px;font-weight:700;color:var(--accent-red);white-space:nowrap}
  .parts-list li::before{content:"";width:14px;height:14px;border-radius:50%;background:var(--navy);flex:none}

  .product-shot{position:absolute;border-radius:50%;border:4px solid var(--ring-blue);
    background:radial-gradient(circle at 50% 50%,#ffffff 0%,#eef3f8 70%,#dbe6f1 100%)}
  .product-shot .fill{position:absolute;inset:18%;border-radius:40%}
  .shot-valve{left:262px;top:415px;width:118px;height:118px}
  .shot-valve .fill{background:linear-gradient(180deg,#c9a86a,#8c6b3a)}
  .shot-jockey{left:412px;top:410px;width:118px;height:118px}
  .shot-jockey .fill{inset:14% 34%;background:linear-gradient(180deg,#e6d6b6,#9aa4ae 60%,#5d7fa8)}
  .shot-pump{left:330px;top:512px;width:130px;height:130px}
  .shot-pump .fill{inset:24% 12%;background:linear-gradient(90deg,#b31b24,#e02a33,#8e1219)}

  .contact{position:absolute;left:28px;top:724px;font-size:14px;color:var(--text-dark);white-space:nowrap}
  .contact strong{font-weight:700}
  .contact .sep{margin:0 8px}
</style>
</head>
<body>
  <article class="flyer">
    <div class="hero-photo" role="img" aria-label="Fire pump room with red pumps, valves and piping"></div>
    <h1 class="headline">Fire Pump Repair Parts<br>&amp; Accessories!</h1>

    <div class="maker-grid">
      <div class="maker-tile">Halden</div>
      <div class="maker-tile">Corvel Works</div>
      <div class="maker-tile">Brightwater</div>
      <div class="maker-tile">Nordavik</div>
      <div class="maker-tile red">Ashgrove</div>
      <div class="maker-tile red">Keystride</div>
      <div class="maker-tile">Lumora</div>
      <div class="maker-tile red">Vantrell</div>
    </div>

    <svg class="panel-shape" width="600" height="776" viewBox="0 0 600 776" aria-hidden="true">
      <path d="M0 400 L150 400 C185 400 180 352 215 352 L600 352 L600 776 L0 776 Z" fill="#ffffff"/>
      <path d="M0 400 L150 400 C185 400 180 352 215 352 L600 352" fill="none" stroke="#1f3a93" stroke-width="5"/>
    </svg>

    <div class="footer-photo" role="img" aria-label="Technician's hands tightening a pipe fitting"></div>
    <div class="footer-fade"></div>

    <svg class="footer-rule" width="600" height="776" viewBox="0 0 600 776" aria-hidden="true">
      <path d="M0 698 L440 698 C470 698 465 672 495 672 L600 672" fill="none" stroke="#e0213a" stroke-width="3"/>
    </svg>

    <div class="brand">
      <span class="brand-square"></span>
      <span class="brand-name">Meridian Valvecraft Supply</span>
    </div>

    <ul class="parts-list">
      <li>Fire Pump Repack Kits</li>
      <li>Jockey Pumps</li>
      <li>Pump Controllers</li>
      <li>Casing Relief Valves</li>
      <li>Air Release Valves</li>
      <li>Suction / Discharge Gauges</li>
      <li>Flow Meters</li>
      <li>Pump Shaft Couplers &amp; Shim Kits</li>
      <li>Fire Pump Relief Valves</li>
      <li>QN Listed Pressure Reducing Valves</li>
    </ul>

    <div class="product-shot shot-valve" role="img" aria-label="Brass pressure reducing valve"><div class="fill"></div></div>
    <div class="product-shot shot-jockey" role="img" aria-label="Vertical multistage jockey pump"><div class="fill"></div></div>
    <div class="product-shot shot-pump" role="img" aria-label="Red split-case fire pumps"><div class="fill"></div></div>

    <p class="contact">Call Us Today: <strong>(800) 431-2867</strong><span class="sep">|</span><strong>www.tolvenspares.example</strong></p>
  </article>
</body>
</html>
```